Long Term Contract - Wordpress Designers Wanted!

We are rapidly growing start-up web development company, focused on website development geared towards the insurance industry.

To increase our impact, we’ve decided to add a freelance designer to the team to assist in graphical elements and webdesign for our clients and template development.

This is to screen for a LONG TERM relationship where we will work together to design and develop sites for insurance agents. We are seeking a talented web designer with experience in WordPress and WordPress theme development to work his/her magic on our new websites.

To win this contest, please create an example website design for an individual insurance agent that sells auto and home insurance. The website will essentially be a "business card" for the agent and will generate trust, show experience, and most importantly create a call to action for the person to call or get a quote.

An example is here:

http://plovermarsh.example/heron/

As part of the deliverable, we will want you to integrate these templates as child themes under Quillmorph "Trellis" template framework - which we can provide you of course. All forms should be done in gravity forms.

Target Market(s)

Audience: consumers shopping for insurance agent

Industry/Entity Type

Insurance

Requirements
Must have
• Pages:
-home
-products
-about
-news/blog
-Contact us

On home page the following elements should be included:
-contact us form
-agent contact information
-blog entries
-testimonial
-agency overview
Should not have
• flash

```html
<!DOCTYPE html>
<html lang="en">
<head>
<meta charset="utf-8">
<title>Ridgefield Cover</title>
<link rel="stylesheet" href="https://fonts.googleapis.com/css2?family=Arimo:wght@400;700&family=Oswald:wght@400;500&family=Roboto+Condensed:wght@300;700&family=Tinos:ital@0;1&display=swap">
<style>
:root{
  --page:#e6e7e9;
  --topbar:#b5b6b8;
  --panel:#c9cacc;
  --blue:#1a9ad6;
  --sky:#5aa6d9;
  --red:#e0301e;
  --ink:#3a3a3a;
  --white:#fff;
  --navy:#07305c;
  --navy-deep:#041f40;
}
*{box-sizing:border-box;margin:0;padding:0}
html,body{width:815px;height:1200px;overflow:hidden}
body{position:relative;background:var(--page);font-family:Arimo,Arial,sans-serif;color:var(--ink)}
.abs{position:absolute}
.topbar{left:0;top:0;width:815px;height:20px;background:var(--topbar)}
.toplinks{right:38px;top:5px;font-size:8px;color:#444}
.toplinks b{color:#333}
.brand{left:118px;top:55px;font-family:Arimo,Arial,sans-serif;font-weight:700;font-size:28px;color:var(--blue);line-height:1;white-space:nowrap}
.lang-label{left:499px;top:57px;font-size:10px;color:#555}
.select{background:var(--white);border:1px solid #d5d5d5;font-size:9px;color:#777;padding-left:9px;display:flex;align-items:center}
.select .caret{position:absolute;right:3px;top:3px;width:14px;height:14px;background:var(--blue);border-radius:2px}
.nav{left:105px;top:111px;width:605px;height:29px;background:linear-gradient(#d3d4d6,#c4c5c7);border-radius:5px 5px 0 0;display:flex}
.nav a{font-family:"Roboto Condensed",sans-serif;font-weight:700;font-size:11px;color:#444;text-decoration:none;display:flex;align-items:center;padding:0 16px;border-right:1px solid #b5b6b8;height:29px}
.nav a.active{color:#2b4a9a}
.search{left:541px;top:114px;width:133px;height:23px;background:var(--white);font-size:9px;color:#888;padding:7px 0 0 9px;border-radius:2px 0 0 2px}
.search-btn{left:674px;top:114px;width:22px;height:23px;background:var(--blue);border-radius:0 2px 2px 0}
.hero{left:105px;top:140px;width:605px;height:310px;background:var(--panel);border-radius:0 0 6px 6px}
.photo{background:linear-gradient(160deg,#5ea4de,#9cc8ee 55%,#e9eef2)}
.dots{left:145px;top:425px;display:flex;gap:5px}
.dots span{width:9px;height:9px;border-radius:50%;background:#ddd;border:1px solid #999}
.dots span:first-child{background:var(--blue)}
.callhead{left:522px;top:150px;width:176px;height:36px;background:var(--sky);border-bottom:2px solid #3b6d93;font-family:Oswald,sans-serif;font-weight:500;font-size:19px;color:var(--white);text-align:center;line-height:36px}
.callnote{left:546px;top:199px;width:132px;font-size:7.5px;color:#555;line-height:1.3;padding-bottom:5px;border-bottom:1px solid #aaa}
.field{background:var(--white);border:1px solid #d3d3d3;border-radius:2px;font-size:8.5px;color:#666;padding-left:9px;display:flex;align-items:center}
.field i{color:var(--red);font-style:normal;margin-left:2px}
.example{left:600px;top:320px;font-size:6.5px;color:#555}
.send-req{left:550px;top:374px;width:124px;height:29px;background:var(--red);color:var(--white);font-family:Oswald,sans-serif;font-size:17px;text-align:center;line-height:29px;border-radius:2px}
.privacy{left:550px;top:411px;font-size:7.5px;color:#555;line-height:1.4}
.privacy span{color:var(--blue)}
.card-img{height:87px}
.card-text{width:130px;font-size:9.5px;line-height:14px;color:#444}
.more{font-size:7.5px;color:var(--blue)}
.btn-blue{background:var(--blue);color:var(--white);font-family:Tinos,serif;font-size:12px;text-align:center;line-height:25px;height:25px}
.news-title{left:554px;top:465px;font-size:17px;font-weight:700;color:var(--blue)}
.news-rule{left:542px;top:488px;width:168px;height:1px;background:#bbb}
.news{left:543px;top:498px;list-style:none;font-size:7.5px;color:#666}
.news li{height:16.2px}
.news li::before{content:">";color:var(--red);margin-right:5px}
.about-title{left:118px;top:690px;font-size:27px;font-weight:700;color:var(--blue);letter-spacing:1.5px}
.about-text{left:117px;top:724px;width:405px;font-size:12px;line-height:19px;color:#444;letter-spacing:.75px}
.about-text span{color:var(--blue)}
.btn-light{background:#f1f1f2;border:1px solid #ccc;border-radius:2px;font-family:Tinos,serif;font-size:11px;color:#555;text-align:center}
.quote{left:117px;top:864px;width:391px;height:82px;border:1px solid #d3d4d6;border-radius:4px}
.quote p{position:absolute;left:42px;top:20px;width:340px;font-family:Tinos,serif;font-style:italic;font-size:11px;line-height:18px;color:#555;letter-spacing:.3px}
.quote .who{position:absolute;left:42px;top:66px;font-size:8.5px;color:#555}
.quote .mark{position:absolute;font-family:Tinos,serif;font-size:34px;color:#666;line-height:1}
.contact{left:543px;top:690px;width:166px;height:256px;border:1px solid #d3d4d6;border-radius:4px}
.contact-inner{left:547px;top:694px;width:158px;height:248px;border:1px solid #d3d4d6;border-radius:3px}
.contact-title{left:543px;top:700px;width:166px;text-align:center;font-family:"Roboto Condensed",sans-serif;font-weight:300;font-size:23px;color:#555}
.ticker{left:0;top:967px;width:815px;height:32px;background:linear-gradient(#0c4b86,#0a3a6c);font-size:8px;color:var(--white);padding:11px 0 0 121px}
.ticker span{color:#7fc3ee}
.footer{left:0;top:999px;width:815px;height:201px;background:radial-gradient(ellipse at 40% 20%,#0d4a86,var(--navy) 55%,var(--navy-deep))}
.fcol{font-size:7.5px;color:var(--white);line-height:13.6px}
.fcol h3{font-size:13px;color:#5ab3ea;margin-bottom:4px;line-height:15px}
.news-sign{left:379px;top:1035px;font-size:14px;font-weight:700;color:var(--white)}
.f-email{left:377px;top:1063px;width:149px;height:23px;background:var(--white);border-radius:3px;font-size:9px;color:#888;padding:7px 0 0 9px}
.subscribe{left:536px;top:1063px;width:74px;height:23px;background:var(--red);border-radius:3px;color:var(--white);font-weight:700;font-size:11px;text-align:center;line-height:23px}
.social{left:640px;top:1064px;display:flex;gap:3px}
.social span{width:21px;height:21px;background:#d8d9db;border-radius:3px}
.frule{left:0;top:1133px;width:815px;height:1px;background:#1d5a92}
.legal{left:119px;top:1149px;font-size:7.5px;color:var(--white)}
.copy{left:119px;top:1162px;font-size:7.5px;color:#3ba0e3}
</style>
</head>
<body>
<div class="abs topbar"></div>
<div class="abs toplinks"><b>Login</b> &nbsp;|&nbsp; Register &nbsp;|&nbsp; FAQ</div>

<div class="abs brand">Ridgefield Cover</div>
<div class="abs lang-label">Select Language</div>
<div class="abs select" style="left:582px;top:53px;width:112px;height:19px">English<span class="caret"></span></div>

<nav class="abs nav">
  <a class="active" href="#">HOME</a><a href="#">PRODUCTS</a><a href="#">ABOUT US</a><a href="#">NEWS</a><a href="#">BLOG</a><a href="#">CONTACT US</a>
</nav>
<div class="abs search">Search...</div>
<div class="abs search-btn">
  <svg width="22" height="23" viewBox="0 0 22 23"><circle cx="12" cy="9" r="4" fill="none" stroke="#fff" stroke-width="2"/><line x1="10" y1="12" x2="6" y2="18" stroke="#fff" stroke-width="2.5"/></svg>
</div>

<div class="abs hero"></div>
<div class="abs photo" style="left:115px;top:150px;width:407px;height:288px" role="img" aria-label="Smiling family of four in white shirts against a blue sky"></div>
<div class="abs dots"><span></span><span></span><span></span><span></span></div>

<div class="abs callhead">LET US CALL YOU</div>
<div class="abs callnote">Please fill out this form, and we'll call you as soon as possible.</div>
<div class="abs field" style="left:546px;top:234px;width:132px;height:22px">Name<i>*</i></div>
<div class="abs field" style="left:546px;top:263px;width:132px;height:22px">Email<i>*</i></div>
<div class="abs field" style="left:546px;top:294px;width:52px;height:22px">Country<i>*</i></div>
<div class="abs field" style="left:600px;top:294px;width:78px;height:22px">Number<i>*</i></div>
<div class="abs example">Example: +1 123 123456</div>
<div class="abs field select" style="left:546px;top:341px;width:132px;height:21px">Select Country<i>*</i><span class="caret"></span></div>
<div class="abs send-req">SEND REQUEST</div>
<div class="abs privacy">We respect your privacy. <span>Click here</span><br><span>to obtain our privacy policy &gt;&gt;</span></div>

<div class="abs card-img" style="left:114px;top:469px;width:131px;background:linear-gradient(135deg,#c9c9c9,#777 60%,#4a4a4a)" role="img" aria-label="Woman driving a car"></div>
<div class="abs card-img" style="left:250px;top:469px;width:132px;background:linear-gradient(#8cb4dc,#d8d2c4 45%,#5f8a3a)" role="img" aria-label="Family in front of their house"></div>
<div class="abs card-img" style="left:388px;top:469px;width:133px;background:linear-gradient(135deg,#d8c7b3,#c4362d 50%,#e6d8c8)" role="img" aria-label="House keys handed over at a sold sign"></div>

<div class="abs card-text" style="left:117px;top:570px">Nulla venenatis. In pede mi, aliquet sit amet, euismod in, auctor ut, ligula.</div>
<div class="abs card-text" style="left:254px;top:570px">Nulla venenatis. In pede mi, aliquet sit amet, euismod in, auctor ut, ligula.</div>
<div class="abs card-text" style="left:393px;top:570px">Nulla venenatis. In pede mi, aliquet sit amet, euismod in, auctor ut, ligula.</div>
<div class="abs more" style="left:117px;top:618px">Learn More &gt;&gt;</div>
<div class="abs more" style="left:254px;top:618px">Learn More &gt;&gt;</div>
<div class="abs more" style="left:393px;top:618px">Learn More &gt;&gt;</div>
<div class="abs btn-blue" style="left:117px;top:636px;width:104px">Get a Free Quote</div>
<div class="abs btn-blue" style="left:254px;top:636px;width:104px">Get a Free Quote</div>
<div class="abs btn-blue" style="left:393px;top:636px;width:104px">Find an Agent</div>

<div class="abs news-title">Latest News</div>
<div class="abs news-rule"></div>
<ul class="abs news">
  <li>Aliquam dapibus tincidunt metus ..</li>
  <li>Praesent justo dolor sagittis euismod..</li>
  <li>Vestibulum sed ante</li>
  <li>Donec sagittis euismod purus</li>
  <li>Praesent justo dolor sagittis ...</li>
  <li>Aliquam dapibus tincidunt metus ..</li>
  <li>Praesent justo dolor sagittis euismod..</li>
  <li>Vestibulum sed ante</li>
</ul>
<div class="abs btn-blue" style="left:552px;top:636px;width:104px">See More &gt;&gt;</div>

<div class="abs about-title">About Ridgefield Cover</div>
<div class="abs about-text">Aliquam congue fermentum nisl. Mauris accumsan nulla vel diam. Sed in lacus ut enim <span>adipiscing</span> aliquet.&nbsp; Nulla venenatis. In pede mi, aliquet sit amet, euismod in, auctor ut, ligula. Aliquam dapibus tincidunt metus. Praesent justo dolor.</div>
<div class="abs btn-light" style="left:117px;top:810px;width:78px;height:25px;line-height:23px">Read More</div>

<div class="abs quote">
  <span class="mark" style="left:16px;top:10px">&ldquo;</span>
  <p>Nulla venenatis. In pede mi, aliquet sit amet, euismod in, auctor ut, ligula. Aliquam dapibus tincidunt metus. Praesent justo dolor.</p>
  <span class="mark" style="left:354px;top:44px">&rdquo;</span>
  <span class="who">--Dale Whitcombe Home Owner, NH</span>
</div>

<div class="abs contact"></div>
<div class="abs contact-inner"></div>
<div class="abs contact-title">Contact Us</div>
<div class="abs field" style="left:564px;top:741px;width:126px;height:22px;font-size:8px">Name<i>*</i></div>
<div class="abs field" style="left:564px;top:769px;width:126px;height:21px;font-size:8px">Email<i>*</i></div>
<div class="abs field" style="left:564px;top:795px;width:126px;height:104px;font-size:8px;align-items:flex-start;padding-top:7px">Message<i>*</i></div>
<div class="abs btn-light" style="left:631px;top:910px;width:58px;height:20px;line-height:19px">SEND</div>

<div class="abs ticker">Corwin P. on <span>Recent Blog</span> "Aliquam dapibus tincidunt metus donec sagittis, praesent justo dolor sagittis euismod purus..". <span>Edwin Tallis</span> &nbsp;&nbsp;&nbsp;<span>3 days ago</span></div>

<footer class="abs footer"></footer>
<div class="abs fcol" style="left:119px;top:1035px"><h3>About Us</h3>Company Info<br>Our Services<br>Clients<br>Partners</div>
<div class="abs fcol" style="left:218px;top:1035px"><h3>Advice</h3>Sign up<br>Forums<br>Promotion<br>Career</div>
<div class="abs fcol" style="left:303px;top:1035px"><h3>Join In</h3>FAQs<br>Solutions<br>Sitemap<br>Contacts</div>
<div class="abs news-sign">Join our Newsletter</div>
<div class="abs f-email">Email Address:</div>
<div class="abs subscribe">Subscribe</div>
<div class="abs social"><span></span><span></span><span></span></div>
<div class="abs frule"></div>
<div class="abs legal">Disclaimer &amp; Terms &amp; Conditions &nbsp;|&nbsp; Privacy Policy &nbsp;|&nbsp; Advertise With Us &nbsp;|&nbsp; Contact Us</div>
<div class="abs copy">Ridgefield Cover &nbsp;&copy; 2012. &nbsp;All Rights Reserved</div>
</body>
</html>
```